Rack card for a integrative medical practice

Need an eye-catching rack card with our logo with content as provided. We have a membership based holistic medical practice which incorporates western and holistic medicine. We would like to focus on wellness and healthy lifestyle. See uploaded files for what is included in the membership. Would like 2 page rack card color on both sides. Logo must be on the front.

Target Market(s)

People looking for alternative medicine, healthy lifestyle.

Industry/Entity Type

Health and Wellness

Colors
00AB8E
00BBA5
67D7C9
C6EFE9
E9F9F6

Requirements
Must have
• Must spark interest at first sight. Clear message.
Nice to have
• Warm, bright and positive vibe. Organic, neutral and earthy colors.
Should not have
• Traditional medical practice vibe (cold, formal, industrial). No PINK except the logo.

```html
<!DOCTYPE html>
<html lang="en">
<head>
<meta charset="utf-8">
<title>Fernleaf Health &amp; Wellness – Rack Card</title>
<link href="https://fonts.googleapis.com/css2?family=Marcellus&family=Libre+Baskerville:wght@700&display=swap" rel="stylesheet">
<style>
  :root {
    --teal-deep: #00AB8E;
    --teal: #00BBA5;
    --mint: #67D7C9;
    --mint-soft: #C6EFE9;
    --mint-pale: #E9F9F6;
    --ink-green: #0f3d36;
    --page: #f2f2f2;
    --white: #ffffff;
  }
  * { box-sizing: border-box; margin: 0; padding: 0; }
  html, body { width: 1200px; height: 1037px; overflow: hidden; }
  body {
    position: relative;
    background: var(--page);
    font-family: "Marcellus", serif;
    color: var(--teal-deep);
  }
  .side-label {
    position: absolute;
    top: 155px;
    width: 200px;
    text-align: center;
    font-family: "Libre Baskerville", serif;
    font-weight: 700;
    font-size: 22px;
    color: #111;
    letter-spacing: 0.5px;
  }
  .side-label--front { left: 288px; }
  .side-label--back { left: 716px; }

  .card {
    position: absolute;
    top: 222px;
    width: 296px;
    height: 660px;
    overflow: hidden;
  }

  /* FRONT */
  .card--front {
    left: 240px;
    background: linear-gradient(to bottom, var(--white) 0%, var(--white) 14%, var(--mint-pale) 30%, var(--mint-soft) 62%, var(--mint) 100%);
  }
  .brand {
    position: absolute;
    top: 42px; left: 0; right: 0;
    text-align: center;
    color: var(--ink-green);
  }
  .brand__mark {
    width: 44px; height: 44px;
    margin: 0 auto 10px;
    border-radius: 50%;
    background: var(--ink-green);
  }
  .brand__name {
    font-size: 28px;
    letter-spacing: 5px;
    line-height: 1;
  }
  .brand__tag {
    margin-top: 4px;
    font-size: 7px;
    letter-spacing: 2.5px;
  }
  .hero-photo {
    position: absolute;
    top: 152px; left: 0;
    width: 296px; height: 258px;
  }
  .front-panel {
    position: absolute;
    top: 380px; left: 24px;
    width: 247px; height: 280px;
    background: linear-gradient(to bottom, var(--mint-pale), var(--mint-soft) 45%, var(--mint) 100%);
  }
  .front-message {
    position: absolute;
    top: 445px; left: 0; right: 0;
    text-align: center;
    font-size: 15.5px;
    letter-spacing: 1.2px;
    line-height: 27.8px;
    text-transform: uppercase;
    color: var(--teal-deep);
  }
  .front-message .highlight {
    display: inline-block;
    padding: 0 14px;
    line-height: 19px;
    background: var(--teal-deep);
    color: var(--white);
  }
  .address-bar {
    position: absolute;
    top: 631px; left: 16px;
    width: 262px; height: 19px;
    background: var(--teal-deep);
    color: var(--white);
    font-size: 12.5px;
    line-height: 19px;
    text-align: center;
  }

  /* BACK */
  .card--back {
    left: 668px;
    background: linear-gradient(to bottom, var(--white) 0%, var(--mint-pale) 30%, var(--mint) 75%, var(--teal-deep) 100%);
  }
  .back-heading {
    position: absolute;
    top: 42px; left: 0;
    font-size: 16.5px;
    font-weight: 400;
    letter-spacing: 0.8px;
    line-height: 25px;
    text-transform: uppercase;
  }
  .back-heading__line { display: block; padding-left: 14px; }
  .back-heading__line--boxed {
    width: 198px;
    padding-left: 14px;
    background: var(--teal-deep);
    color: var(--white);
  }
  .benefits-panel {
    position: absolute;
    top: 88px; left: 11px;
    width: 273px; height: 556px;
    background: linear-gradient(to bottom, var(--white) 0%, var(--white) 40%, var(--mint-soft) 80%, var(--mint) 100%);
  }
  .benefits {
    position: absolute;
    left: 14px; width: 252px;
    list-style: none;
    font-size: 13px;
    line-height: 21px;
    color: var(--teal-deep);
  }
  .benefits li {
    position: absolute;
    left: 0; width: 252px;
    padding-left: 12px;
  }
  .benefits li::before {
    content: "";
    position: absolute;
    left: 0; top: 8px;
    width: 5px; height: 5px;
    border-radius: 50%;
    background: var(--teal-deep);
  }
</style>
</head>
<body>

  <div class="side-label side-label--front">FRONT</div>
  <div class="side-label side-label--back">BACK</div>

  <section class="card card--front">
    <div class="brand">
      <div class="brand__mark"></div>
      <div class="brand__name">FERNLEAF</div>
      <div class="brand__tag">HEALTH &amp; WELLNESS</div>
    </div>

    <svg class="hero-photo" role="img" aria-label="Photo of a relaxed person in light clothing sitting cross-legged on a patterned blanket" viewBox="0 0 296 258">
      <defs>
        <linearGradient id="heroTone" x1="0" y1="0" x2="1" y2="1">
          <stop offset="0" stop-color="#d9c9cf"/>
          <stop offset="0.5" stop-color="#efe6e4"/>
          <stop offset="1" stop-color="#c9a9ad"/>
        </linearGradient>
      </defs>
      <rect width="296" height="258" fill="url(#heroTone)"/>
    </svg>

    <div class="front-panel"></div>

    <p class="front-message">
      A direct primary<br>
      care practice<br>
      focused on a<br>
      <span class="highlight">more</span><br>
      holistic and personal<br>
      approach to medicine.
    </p>

    <div class="address-bar">1420 W Elm St. STE 2B Brookdale</div>
  </section>

  <section class="card card--back">
    <h2 class="back-heading">
      <span class="back-heading__line">Whats included in</span>
      <span class="back-heading__line back-heading__line--boxed">Your membership :</span>
    </h2>

    <div class="benefits-panel">
      <ul class="benefits">
        <li style="top:24px">Unlimited office visits with no copay Direct communication with your doctor</li>
        <li style="top:106px">Discounted labs, imaging and medications</li>
        <li style="top:170px">Free initial acupuncture session ($250 value).</li>
        <li style="top:233px">2 Kinetra testings per year ($100 value)</li>
        <li style="top:275px">Discounts for supplements and health products in the clinic</li>
        <li style="top:337px">Discounts for iv vitamin infusion therapy</li>
        <li style="top:401px">Personalized nutrition plan after advanced testing such as gut microbiome, hormonal, metabolism test, etc.</li>
      </ul>
    </div>
  </section>

</body>
</html>
```